Talvor GmbH business card

We Talvor GmbH based in Switzerland are looking for a business card design. The Fresh Jung, appealing to customers of all kinds. We already have a logo to upload but still a business card. Details: Talvor GmbH Address: Lindenweg 14b in 9476 Brugwil. Tel: 41 79 462 37 18, web: Talvor.ch, E-mail: info@Talvor.ch Facebook: Talvor GmbH. I am the Managing Director: Luka Petrovac. On reverse: Title: Transporter and bus rental Gross: Without deposit Super prices
Contact Information for Business Card
Siehe Projektbeschreibung
Requirements
Should not have
- Other pictures

```html
<!DOCTYPE html>
<html lang="de">
<head>
<meta charset="utf-8">
<title>Talvor GmbH – Visitenkarte</title>
<link rel="stylesheet" href="https://fonts.googleapis.com/css2?family=Roboto:wght@300;400;500&family=Montserrat:wght@700&display=swap">
<style>
  :root {
    --page-bg: #b9b9b9;
    --card-white: #f7f7f7;
    --card-black: #141414;
    --navy: #34337f;
    --steel: #8ea4bd;
    --text-dark: #3a3a3a;
    --text-mid: #555555;
  }
  * { box-sizing: border-box; margin: 0; padding: 0; }
  html, body { width: 1200px; height: 1200px; overflow: hidden; }
  body {
    background: linear-gradient(180deg, #9c9c9c 0%, #d6d6d6 100%);
    font-family: "Roboto", Arial, sans-serif;
    position: relative;
  }
  .card {
    position: absolute;
    left: 180px;
    width: 840px;
    height: 480px;
    box-shadow: 0 10px 30px rgba(0,0,0,0.25);
  }
  .card--back { top: 90px; background: var(--card-black); display: flex; align-items: center; justify-content: center; }
  .card--front { top: 630px; background: var(--card-white); }

  .brand { display: flex; align-items: center; gap: 18px; }
  .brand__mark { width: 44px; height: 44px; background: var(--navy); }
  .brand__name {
    font-family: "Montserrat", Arial, sans-serif;
    font-weight: 700;
    font-size: 64px;
    letter-spacing: 2px;
    color: var(--navy);
  }
  .card--back .brand__name { color: #4a4aa8; font-size: 78px; }
  .card--back .brand__mark { background: #4a4aa8; width: 54px; height: 54px; }

  .front__logo {
    position: absolute;
    left: 0; top: 0;
    width: 440px; height: 480px;
    display: flex; flex-direction: column; align-items: center; justify-content: center;
    gap: 14px;
  }
  .front__logo .brand__name { font-size: 56px; }
  .tagline { font-size: 21px; font-weight: 300; color: var(--text-mid); }

  .divider { position: absolute; left: 452px; top: 70px; width: 2px; height: 340px; background: var(--navy); }

  .front__info { position: absolute; left: 488px; top: 78px; right: 30px; color: var(--text-dark); }
  .person__name { font-size: 30px; font-weight: 300; color: var(--text-dark); }
  .person__role { font-size: 18px; font-weight: 300; color: #5b5bb0; margin-top: 2px; }
  .address { font-size: 20px; font-weight: 300; margin-top: 70px; }
  .contact { list-style: none; margin-top: 22px; }
  .contact li { display: flex; align-items: center; gap: 12px; font-size: 20px; font-weight: 300; line-height: 34px; }
  .contact svg { width: 18px; height: 18px; flex: none; }
</style>
</head>
<body>
  <section class="card card--back" aria-label="Rückseite">
    <div class="brand">
      <span class="brand__mark"></span>
      <span class="brand__name">Talvor GmbH</span>
    </div>
  </section>

  <section class="card card--front" aria-label="Vorderseite">
    <div class="front__logo">
      <div class="brand">
        <span class="brand__mark"></span>
        <span class="brand__name">Talvor GmbH</span>
      </div>
      <p class="tagline">Transporter und Bus Vermietung</p>
    </div>

    <div class="divider"></div>

    <div class="front__info">
      <p class="person__name">Nadia Brenner</p>
      <p class="person__role">Owner</p>
      <p class="address">Lindenweg 14b in 9476 Brugwil</p>
      <ul class="contact">
        <li>
          <svg viewBox="0 0 18 18"><rect width="18" height="18" rx="2" fill="#34337f"/><path d="M5 4.5l2 0 1 3-1.3 1a6 6 0 0 0 2.8 2.8l1-1.3 3 1 0 2a1 1 0 0 1-1 1A9 9 0 0 1 4 5.5a1 1 0 0 1 1-1z" fill="#fff"/></svg>
          +41 79 462 37 18
        </li>
        <li>
          <svg viewBox="0 0 18 18"><rect width="18" height="18" rx="2" fill="#34337f"/><circle cx="9" cy="9" r="5" fill="none" stroke="#fff" stroke-width="1.3"/><path d="M4 9h10M9 4c-2.5 3-2.5 7 0 10M9 4c2.5 3 2.5 7 0 10" fill="none" stroke="#fff" stroke-width="1"/></svg>
          www.Talvor.ch
        </li>
        <li>
          <svg viewBox="0 0 18 18"><rect width="18" height="18" rx="2" fill="#34337f"/><rect x="4" y="5.5" width="10" height="7" fill="none" stroke="#fff" stroke-width="1.2"/><path d="M4 5.5l5 4 5-4" fill="none" stroke="#fff" stroke-width="1.2"/></svg>
          info@Talvor.ch
        </li>
        <li>
          <svg viewBox="0 0 18 18"><rect width="18" height="18" rx="2" fill="#34337f"/></svg>
          Talvor GmbH
        </li>
      </ul>
    </div>
  </section>
</body>
</html>
```